Off Grid consulting and outdoor products needs a website

We need a website design to help launch our new business. Its a business that plans to offer Off-grid conslting and outdoor survival products to people who are looking to relocate or vacation to properties/homes that are Off-grid. We plan to offer design plans for homes/cabins, renewable energy systems for power/heating etc, survival products for outdoor vacations/living. We also do consulting and project management for those who want to design and build from scratch their dream off-grid home or vacation property. I've included our logo design for use.
Would like the website to include 5 pages.
www.bramblequietlands.com
The main landing page (1)
want a video loop backround with a flyover of a cabin in the woods.
https://www.clipvaultmedia.com/video/clip-48213307-pale-sky-thawing-frost-on-pine-slope
(also need a backup static image of just high-shot of cabin in woods)
logo top left, Quoted string of text in the middle, over the video. and a CTA button to 'Contact us'
picture links below that to last 3 recent blog posts.
About Us page (2)
(example) https://larkhollowgear.com/pages/about-lark
Blog page (3)
blog posts associated with pictures.
Consulting 'services' page (4)
-land services and moving off-grid
-Building off grid
-Renewable energy off-grid
-Sustainable farming and all season greenhouses
Store page 'comming soon' (5)
(Example) http://hearthkeep.quillstheme.com/demo-1/demo.html

Target Market(s)

Outdoor enthusiasts and people who want to escape their city life

Coding

Coded - Design and coding required

Requirements
Must have
• Outdoor feel, woods, cabin, reneable energy (solar, geothermal, greenhouses, water wells)

```html
<!DOCTYPE html>
<html lang="en">
<head>
<meta charset="utf-8">
<title>Bramble Quietlands</title>
<link href="https://fonts.googleapis.com/css2?family=Oswald:wght@500;600;700&family=Roboto:ital,wght@0,400;0,500;1,400&family=Inter:wght@400;600&display=swap" rel="stylesheet">
<style>
:root{
  --ink:#000;
  --heading:#222;
  --white:#fff;
  --moss:#5e6b5e;
  --moss-deep:#535f53;
  --moss-soft:#7a867a;
  --mist:#efefef;
  --date:#5e6b5e;
  --body:#444;
}
*{margin:0;padding:0;box-sizing:border-box}
html,body{width:1200px;height:3394px;overflow:hidden;background:var(--white)}
body{position:relative;font-family:'Roboto',sans-serif;color:var(--heading)}
.abs{position:absolute}
.oswald{font-family:'Oswald',sans-serif;font-weight:700;text-transform:uppercase}

/* header */
.site-header{left:0;top:0;width:1200px;height:86px;background:var(--ink);z-index:3}
.brand-plate{left:0;top:0;width:370px;height:166px;z-index:4}
.brand-name{left:126px;top:28px;z-index:5;color:var(--white);font-family:'Oswald',sans-serif;font-weight:700;font-size:30px;line-height:34px;text-transform:uppercase;letter-spacing:.5px}
.main-nav a{position:absolute;top:30px;color:var(--white);text-decoration:none;font-family:'Oswald',sans-serif;font-weight:600;font-size:17px;text-transform:uppercase}
.call{left:914px;top:22px;z-index:5;display:flex;align-items:center;gap:12px;color:var(--white);font-family:'Oswald',sans-serif;font-weight:600;font-size:17px;line-height:20px}
.icon-circle{width:34px;height:34px;border-radius:50%;background:var(--moss-soft);display:flex;align-items:center;justify-content:center}

/* hero */
.hero{left:0;top:86px;width:1200px;height:624px;background:linear-gradient(180deg,#7fa6d3 0%,#c9d7e6 22%,#d7dbde 36%,#a4a6a3 48%,#606760 64%,#3b443e 82%,#2d3a35 100%)}
.hero-play{left:548px;top:251px}
.hero-title{left:0;width:1200px;top:362px;text-align:center;font-size:66px;color:#111;letter-spacing:1px}
.hero-cta{left:478px;top:460px;width:244px;height:60px;border:3px solid var(--white);border-radius:30px;background:var(--moss);color:var(--white);font-size:27px;display:flex;align-items:center;justify-content:center}

/* blog */
.section-title{left:0;width:1200px;text-align:center;font-size:44px;color:var(--heading)}
.post{width:281px}
.post-thumb{width:281px;height:250px}
.post-title{margin-top:26px;font-family:'Oswald',sans-serif;font-weight:600;font-size:15.5px;line-height:20px;text-transform:uppercase;color:#222}
.post-date{margin-top:12px;font-family:'Oswald',sans-serif;font-weight:500;font-size:13.5px;color:var(--date)}

/* about */
.about{left:0;top:1333px;width:1200px;height:561px;background:var(--mist)}
.about-photo{left:0;top:0}
.about-title{left:150px;top:105px;font-size:47px;line-height:50px;color:#111}
.about-text{left:150px;top:236px;width:390px;font-size:13px;line-height:20px;color:var(--body)}
.read-more{left:151px;top:396px;width:162px;height:54px;border-radius:27px;background:var(--moss);color:var(--white);font-size:16px;display:flex;align-items:center;justify-content:center}

/* testimonials */
.testimonials{left:0;top:1894px;width:1200px;height:411px;background:var(--moss)}
.testimonials .section-title{top:88px;color:var(--white);font-size:42px}
.quote-mark{left:79px;top:154px}
.quote-text{left:200px;width:800px;top:176px;text-align:center;color:var(--white);font-style:italic;font-size:19.5px;line-height:27.5px}
.quote-author{left:0;width:1200px;top:298px;text-align:center;color:var(--white);font-weight:500;font-size:21px}

/* videos */
.video{width:422px}
.video-thumb{position:relative;width:422px;height:255px}
.video-thumb svg{position:absolute;left:159px;top:75px}
.video-caption{margin-top:26px;text-align:center;font-family:'Oswald',sans-serif;font-weight:600;font-size:15.5px;line-height:20px;text-transform:uppercase;color:#444}

/* footer */
.site-footer{left:0;top:2954px;width:1200px;height:440px;background:var(--ink);color:var(--white)}
.footer-head{font-family:'Oswald',sans-serif;font-weight:600;font-size:22px;text-transform:uppercase}
.contact-item{left:188px;display:flex;align-items:center;gap:22px;font-family:'Inter',sans-serif;font-size:15px;line-height:22px}
.contact-item .icon-circle{width:40px;height:40px;background:#4d564d}
.footer-brand{left:440px;top:150px;width:320px;text-align:center;font-family:'Oswald',sans-serif;font-weight:700;font-size:40px;line-height:44px;text-transform:uppercase}
.footer-links a{position:absolute;color:var(--white);text-decoration:none;font-family:'Inter',sans-serif;font-weight:600;font-size:10.5px;text-transform:uppercase}
.legal a,.legal span{position:absolute;top:365px;color:var(--white);text-decoration:none;font-family:'Inter',sans-serif;font-size:13px}
</style>
</head>
<body>

<header>
  <div class="abs site-header"></div>
  <svg class="abs brand-plate" width="370" height="166" viewBox="0 0 370 166"><polygon points="0,0 370,0 370,86 330,86 286,166 0,166" fill="#000"/></svg>
  <div class="abs brand-name">Bramble<br>Quietlands</div>
  <nav class="abs main-nav" style="left:0;top:0;width:1200px;height:86px;z-index:5">
    <a href="#" style="left:355px">Home</a>
    <a href="#" style="left:454px">About Us</a>
    <a href="#" style="left:593px">Blog</a>
    <a href="#" style="left:694px">Services</a>
    <a href="#" style="left:824px">Store</a>
  </nav>
  <div class="abs call">
    <span class="icon-circle"><svg width="16" height="16" viewBox="0 0 24 24"><path fill="#fff" d="M6.6 10.8a15.1 15.1 0 0 0 6.6 6.6l2.2-2.2a1 1 0 0 1 1-.25 11.4 11.4 0 0 0 3.6.57 1 1 0 0 1 1 1V20a1 1 0 0 1-1 1A17 17 0 0 1 3 4a1 1 0 0 1 1-1h3.5a1 1 0 0 1 1 1c0 1.25.2 2.45.57 3.57a1 1 0 0 1-.25 1z"/></svg></span>
    <span>CALL US:<br>5550418827</span>
  </div>
</header>

<section>
  <div class="abs hero" role="img" aria-label="Aerial view of a green cabin with solar panels among snowy pines and mountains"></div>
  <svg class="abs hero-play" width="104" height="104" viewBox="0 0 104 104"><circle cx="52" cy="52" r="48" fill="rgba(255,255,255,.25)" stroke="#fff" stroke-width="6"/><polygon points="40,30 40,74 76,52" fill="#fff"/></svg>
  <h1 class="abs oswald hero-title">Bramble Quietlands</h1>
  <a class="abs oswald hero-cta" href="#">Contact Us</a>
</section>

<section>
  <h2 class="abs oswald section-title" style="top:780px">Latest Blog Posts</h2>
  <article class="abs post" style="left:150px;top:884px">
    <div class="post-thumb" role="img" aria-label="Camper with a rooftop tent in a pine forest" style="background:linear-gradient(135deg,#5e5a44,#c9b88f 45%,#6a5d4c 75%,#2f3a2e)"></div>
    <h3 class="post-title">Lorem ipsum dolor sit ametcoe te tur adipiscing elited do eiumod</h3>
    <p class="post-date">APRIL 12 2022</p>
  </article>
  <article class="abs post" style="left:460px;top:884px">
    <div class="post-thumb" role="img" aria-label="Glass-walled cabin at dusk with two people on the deck" style="background:linear-gradient(160deg,#3b4a3e,#4a4c5e 40%,#b07a3a 65%,#2e2c2a)"></div>
    <h3 class="post-title">Lorem ipsum dolor sit ametcoe te tur adipiscing elited do eiumod</h3>
    <p class="post-date">APRIL 12 2022</p>
  </article>
  <article class="abs post" style="left:768px;top:884px">
    <div class="post-thumb" role="img" aria-label="Solar panel array on green grass under a clear sky" style="background:linear-gradient(180deg,#cfe1f2 0%,#9fc0e0 25%,#1f2d5a 40%,#23305c 68%,#4f8f2e 80%,#3c7a24 100%)"></div>
    <h3 class="post-title">Lorem ipsum dolor sit ametcoe te tur adipiscing elited do eiumod</h3>
    <p class="post-date">APRIL 12 2022</p>
  </article>
</section>

<section class="abs about">
  <svg class="abs about-photo" width="1200" height="561" viewBox="0 0 1200 561" role="img" aria-label="High aerial view of a small cabin in a forest clearing with a person on the path">
    <defs><linearGradient id="forest" x1="0" y1="0" x2="1" y2="1"><stop offset="0" stop-color="#4f5b43"/><stop offset=".5" stop-color="#3e5a4c"/><stop offset="1" stop-color="#5a3f33"/></linearGradient></defs>
    <polygon points="694,0 1200,0 1200,561 589,561" fill="url(#forest)"/>
  </svg>
  <h2 class="abs oswald about-title">About<br>Bramble Quietlands</h2>
  <p class="abs about-text">Lorem ipsum dolor sit amet, consectetur adipiscing elit, sed do eiusmod tempor incididunt ut labore et dolore magna aliqua. Quis ipsum suspendisse ultrices gravida. Risus commodloro viverra maecenas accumsan lacus vel facilisisLorem ipsum dolor sit amet, consectetur adipiscing elit, sed do eiusmolotd tempor incididunt ut labore et dolore magna aliqua. Quis ipsum suspendisse ultrices gravida.</p>
  <a class="abs oswald read-more" href="#">Read More</a>
</section>

<section class="abs testimonials">
  <h2 class="abs oswald section-title">Testimonials</h2>
  <svg class="abs quote-mark" width="114" height="100" viewBox="0 0 114 100"><path fill="#7b857b" d="M4 100V52C4 22 16 6 44 0l4 12C32 18 26 28 26 42h22v58zM66 100V52C66 22 78 6 106 0l4 12C94 18 88 28 88 42h22v58z"/></svg>
  <p class="abs quote-text">“ Lorem ipsum dolor sit amet, consectetur adipiscing elit, sed do eiusmod tempor incididunt ut labore et dolore magna aliqua. Quis ipsum suspendisse ultrices gravida. Risus commodloro viverra maecenas accumsan lacus vel facilisiem ips”</p>
  <p class="abs quote-author">Mara Quillan</p>
</section>

<section>
  <h2 class="abs oswald section-title" style="top:2378px">Offgrid Outdoors Videos</h2>
  <article class="abs video" style="left:158px;top:2513px">
    <div class="video-thumb" role="img" aria-label="Wooden barn below jagged mountains at sunset" style="background:linear-gradient(180deg,#6b5a7a 0%,#d68a6a 30%,#8a8fa0 50%,#5a4a3c 75%,#3d3a2c 100%)">
      <svg width="104" height="104" viewBox="0 0 104 104"><circle cx="52" cy="52" r="47" fill="none" stroke="#fff" stroke-width="6"/><polygon points="40,30 40,74 76,52" fill="#fff"/></svg>
    </div>
    <h3 class="video-caption">Lorem ipsum dolor sit amet, consectetur adipiscing elit, sed do eiusmod tempor incididunt ut</h3>
  </article>
  <article class="abs video" style="left:620px;top:2513px">
    <div class="video-thumb" role="img" aria-label="Two campers in folding chairs by a campfire in a misty meadow" style="background:linear-gradient(180deg,#b9bfc0 0%,#8e9485 30%,#6b7244 60%,#5a5e34 100%)">
      <svg width="104" height="104" viewBox="0 0 104 104"><circle cx="52" cy="52" r="47" fill="none" stroke="#fff" stroke-width="6"/><polygon points="40,30 40,74 76,52" fill="#fff"/></svg>
    </div>
    <h3 class="video-caption">Lorem ipsum dolor sit amet, consectetur adipiscing elit, sed do eiusmod tempor incididunt ut</h3>
  </article>
</section>

<footer class="abs site-footer">
  <h4 class="abs footer-head" style="left:194px;top:80px">Contact</h4>
  <div class="abs contact-item" style="top:145px">
    <span class="icon-circle"><svg width="16" height="16" viewBox="0 0 24 24"><path fill="#fff" d="M6.6 10.8a15.1 15.1 0 0 0 6.6 6.6l2.2-2.2a1 1 0 0 1 1-.25 11.4 11.4 0 0 0 3.6.57 1 1 0 0 1 1 1V20a1 1 0 0 1-1 1A17 17 0 0 1 3 4a1 1 0 0 1 1-1h3.5a1 1 0 0 1 1 1c0 1.25.2 2.45.57 3.57a1 1 0 0 1-.25 1z"/></svg></span>
    <span>Phone<br>+00 5550 3371</span>
  </div>
  <div class="abs contact-item" style="top:199px">
    <span class="icon-circle"><svg width="16" height="14" viewBox="0 0 24 20"><path fill="#fff" d="M2 2h20v3l-10 6L2 5zM2 8l10 6 10-6v10H2z"/></svg></span>
    <span>Email<br>hello@bramblequietlands.com</span>
  </div>
  <div class="abs contact-item" style="top:263px">
    <span class="icon-circle"><svg width="14" height="18" viewBox="0 0 14 20"><path fill="#fff" d="M7 0a7 7 0 0 0-7 7c0 5 7 13 7 13s7-8 7-13a7 7 0 0 0-7-7zm0 10a3 3 0 1 1 0-6 3 3 0 0 1 0 6z"/></svg></span>
    <span>Fernwick Lane, 14<br>4810 Hollowmere</span>
  </div>

  <div class="abs footer-brand">Bramble<br>Quietlands</div>

  <h4 class="abs footer-head" style="left:839px;top:80px">Links</h4>
  <nav class="abs footer-links" style="left:0;top:0;width:1200px;height:300px">
    <a href="#" style="left:835px;top:144px">Home</a>
    <a href="#" style="left:835px;top:177px">About Us</a>
    <a href="#" style="left:835px;top:210px">Blog</a>
    <a href="#" style="left:835px;top:243px">Services</a>
    <a href="#" style="left:835px;top:276px">Store</a>
    <a href="#" style="left:929px;top:144px">Sitemap</a>
    <a href="#" style="left:929px;top:177px">Videos</a>
    <a href="#" style="left:929px;top:210px">Products</a>
    <a href="#" style="left:929px;top:243px">Privacy Policy</a>
    <a href="#" style="left:929px;top:276px">Terms &amp; Conditions</a>
  </nav>

  <div class="abs legal" style="left:0;top:0;width:1200px;height:440px">
    <span style="left:328px">© 2022 &nbsp;All Rights Reserved.</span>
    <a href="#" style="left:520px">User Agreement</a>
    <a href="#" style="left:664px">Privacy Policy</a>
    <a href="#" style="left:789px">Cookie Policy</a>
  </div>
</footer>

</body>
</html>
```